New private nursery in Dubai website design

I need homepage + 1 inner page mockup for a new private nursery website. The nursery is to have a friendly, homely feel and the website should reflect this - It is not a top priority to shout about admissions, however it should be subtle and easily accessible. Simple and clean. Logo attached, however is still being designed so no .ai file available yet. Also attached some themes of the interior of the nursery to give an idea of the look and feel of the place. Check the following website for look and feel

https://lumbrel-orchard.example.com/

https://www.pebblevoss.example.org/about-pebble

https://www.dellawick-tots.example.info/programs

http://www.tarnfieldnursery.example.ae/
Updates

Target Market(s)

parents with young children

Number of Pages Required

3 page

Font styles to use
Sans Serif

Colors
0094D4
00A9DD
6FCCEA
C7EBF8
E9F6FB

Requirements
Must have
• safe, warm, geometric, earthy,

```html
<!DOCTYPE html>
<html lang="en">
<head>
<meta charset="utf-8">
<title>Olvenbrook Nursery</title>
<link rel="stylesheet" href="https://fonts.googleapis.com/css2?family=Roboto:wght@400;500;700&family=Nunito+Sans:wght@700;800;900&display=swap">
<style>
:root{
  --blue:#0094D4;
  --blue-2:#00A9DD;
  --sky:#6FCCEA;
  --ice:#C7EBF8;
  --mist:#E9F6FB;
  --clay:#D48A6E;
  --clay-dark:#C9785C;
  --ink:#1f1f1f;
  --text:#555;
  --footer:#232323;
}
*{box-sizing:border-box;margin:0;padding:0}
html,body{width:1200px;height:4728px;overflow:hidden}
body{position:relative;background:#fff;font-family:"Roboto",sans-serif;color:var(--ink)}
.abs{position:absolute}
.btn{position:absolute;display:flex;align-items:center;justify-content:center;gap:8px;border-radius:30px;color:#fff;font-weight:500;font-size:16px;text-transform:uppercase}
.btn .dot{width:14px;height:14px;border-radius:50%;background:#fff;position:relative}
.btn .dot::after{content:"";position:absolute;left:4px;top:3.5px;border-left:6px solid var(--c);border-top:3.5px solid transparent;border-bottom:3.5px solid transparent}
.section-title{position:absolute;left:0;width:1200px;text-align:center;font-family:"Nunito Sans",sans-serif;font-weight:800;font-size:34px;letter-spacing:.5px}
.section-title::after{content:"";display:block;width:66px;height:3px;background:var(--blue);margin:10px auto 0}
/* header */
.topline{left:0;top:0;width:1200px;height:4px;background:var(--clay)}
.header{left:0;top:4px;width:1200px;height:84px;background:#fff}
.brand{left:110px;top:28px;display:flex;align-items:center;gap:10px;font-family:"Nunito Sans",sans-serif;font-weight:800;font-size:20px;color:var(--clay-dark)}
.brand .mark{width:26px;height:26px;border-radius:50%;background:var(--sky)}
.nav{left:310px;top:38px;display:flex;gap:22px;font-size:15px;color:#333}
.nav .active{color:var(--blue)}
.lang{left:910px;top:38px;font-size:15px;font-weight:700}
.login{left:988px;top:30px;width:99px;height:38px;background:var(--clay);font-size:15px}
/* hero */
.hero{left:0;top:88px;width:1200px;height:650px;background:linear-gradient(100deg,#8f7a68 0%,#c9b6a1 38%,#e2d6c8 60%,#b59a84 100%)}
.hero-kicker{left:112px;top:252px;font-family:"Nunito Sans",sans-serif;font-weight:800;font-size:31px;color:#fff}
.hero-title{left:112px;top:302px;font-family:"Nunito Sans",sans-serif;font-weight:900;font-size:62px;line-height:64px;color:#fff}
.hero-text{left:112px;top:442px;width:470px;font-size:16px;line-height:26px;color:#fff}
.get-started{left:112px;top:518px;width:190px;height:50px;background:var(--clay);--c:var(--clay)}
/* services */
.svc{position:absolute;width:296px;height:296px;border-radius:50%;border:4px solid #fff;color:#fff;text-align:center;padding-top:50px}
.svc.blue{background:var(--blue);--c:var(--blue)}
.svc.clay{background:var(--clay);--c:var(--clay)}
.svc svg{display:block;margin:0 auto}
.svc h3{font-size:19px;font-weight:700;margin-top:14px}
.svc p{font-size:13.5px;line-height:22px;width:232px;margin:12px auto 0}
.svc .more{display:inline-flex;align-items:center;gap:8px;font-weight:700;font-size:14px;margin-top:12px}
.svc .more .dot{width:13px;height:13px;border-radius:50%;background:#fff;position:relative}
.svc .more .dot::after{content:"";position:absolute;left:4px;top:3px;border-left:6px solid var(--c);border-top:3.5px solid transparent;border-bottom:3.5px solid transparent}
/* about */
.about{left:0;top:1300px;width:1200px;height:556px;background:linear-gradient(90deg,#e4f2fa,#f2f8fc 60%,#e9f3f8)}
.about-frame{left:122px;top:1378px;width:288px;height:280px;border:3px solid var(--blue)}
.about-block{left:260px;top:1510px;width:272px;height:266px;background:var(--blue)}
.about-photo{left:140px;top:1402px;width:368px;height:358px;background:linear-gradient(160deg,#b98a72,#9a8a6c 50%,#6f5f4c)}
.about-title{left:610px;top:1370px;font-family:"Nunito Sans",sans-serif;font-weight:800;font-size:34px}
.about-text{left:610px;top:1446px;width:466px;font-size:14.6px;line-height:25.7px;text-align:justify;color:#333}
.about-btn{left:610px;top:1728px;width:190px;height:48px;background:var(--blue);--c:var(--blue)}
/* gallery */
.gallery{left:127px;top:2016px;display:grid;grid-template-columns:repeat(3,298px);grid-auto-rows:214px;gap:18px 25px}
.gallery div{border-radius:2px}
.view-clay{left:504px;top:2510px;width:192px;height:46px;background:var(--clay);--c:var(--clay)}
/* testimonials */
.card{position:absolute;width:408px;height:224px;background:#fff;border-radius:30px;padding:28px 28px 0 96px}
.card .name{font-size:15px;font-weight:500}
.card .stars{color:#f5a623;font-size:17px;letter-spacing:2px;margin-top:2px}
.card p{font-size:13.5px;line-height:23.5px;color:#888;margin-top:6px}
.card .quote{position:absolute;right:32px;top:26px;font-family:"Nunito Sans",sans-serif;font-size:64px;line-height:50px;font-weight:900;color:var(--clay);font-style:normal}
.avatar{position:absolute;width:116px;height:116px;border-radius:50%;border:4px solid #fff}
.arrow{position:absolute;width:20px;height:20px;border-left:3px solid #fff;border-bottom:3px solid #fff}
/* blog */
.blog-main{left:137px;top:3375px;width:441px;height:463px;background:#fff;box-shadow:0 2px 12px rgba(0,0,0,.1);text-align:center}
.blog-main .img{margin:10px 8px 0;height:295px;background:linear-gradient(135deg,#e9e1d8,#c9b9a5 50%,#d98a62)}
.blog-main h4{font-size:16.5px;font-weight:700;margin-top:20px}
.meta{font-size:13px;color:var(--blue);margin-top:8px;display:flex;gap:6px;align-items:center}
.meta .sep{color:#999}
.blog-main .meta{justify-content:center}
.blog-main p{font-size:13px;line-height:22px;color:#666;width:360px;margin:12px auto 0}
.blog-item{position:absolute;left:617px;width:445px;height:135px;background:#fff;box-shadow:0 2px 12px rgba(0,0,0,.1);display:flex;gap:16px;padding:9px}
.blog-item .img{width:152px;height:118px;flex:none}
.blog-item h5{font-size:14.5px;font-weight:500;margin-top:10px}
.blog-item p{font-size:13px;line-height:20px;color:#777;margin-top:8px;width:230px}
.view-blue{left:504px;top:3878px;width:192px;height:48px;background:var(--blue);--c:var(--blue)}
/* newsletter */
.news-title{left:0;top:4112px;width:1200px;text-align:center;font-family:"Nunito Sans",sans-serif;font-weight:800;font-size:34px;color:#fff}
.field{position:absolute;top:4205px;width:283px;height:46px;background:#fff;border-radius:24px;padding-left:24px;display:flex;align-items:center;font-size:13px;color:#777}
.submit{left:824px;top:4205px;width:188px;height:46px;background:var(--clay);font-size:15px}
/* footer */
.footer{left:0;top:4268px;width:1200px;height:460px;background:var(--footer);color:#fff}
.foot-brand{left:112px;top:4400px;display:flex;align-items:center;gap:10px;font-family:"Nunito Sans",sans-serif;font-weight:800;font-size:26px;color:var(--clay)}
.foot-brand .mark{width:32px;height:32px;border-radius:50%;background:var(--sky)}
.social{position:absolute;top:4480px;width:35px;height:35px;border-radius:50%;border:1.5px solid #bbb}
.col{position:absolute;top:4343px}
.col h6{font-size:17px;font-weight:500;margin-bottom:16px}
.col a{display:block;color:#ddd;text-decoration:none;font-size:14px;line-height:38.5px}
.contact-row{display:flex;gap:14px;margin-bottom:14px}
.contact-row svg{flex:none;margin-top:2px}
.contact-row b{display:block;font-size:12px;font-weight:700}
.contact-row span{font-size:14px;line-height:19px;color:#ddd;display:block;margin-top:4px}
.foot-line{left:108px;top:4662px;width:984px;height:1px;background:#555}
.copy{left:0;top:4680px;width:1200px;text-align:center;font-size:13.5px;color:#ddd}
</style>
</head>
<body>

<div class="abs topline"></div>
<header class="abs header"></header>
<div class="abs brand"><span class="mark"></span>Olvenbrook</div>
<nav class="abs nav">
  <span class="active">HOME</span><span>ABOUT US</span><span>SERVICES</span><span>TESTIMONIALS</span><span>BLOG</span><span>CONTACT US</span>
</nav>
<div class="abs lang">ENG &#9662;</div>
<div class="btn login">LOGIN</div>

<section class="abs hero" role="img" aria-label="Photo of a mother and young boy playing with wooden blocks in a bright nursery room"></section>
<div class="abs hero-kicker">WELCOME TO</div>
<h1 class="abs hero-title">AL OLVENBROOK<br>NURSERY</h1>
<p class="abs hero-text">Lorem ipsum dolor sit amet, consectetur adipiscing elit, sed do eiusmod tempor incididunt ut labore et dolore magna</p>
<div class="btn get-started">GET STARTED <span class="dot"></span></div>

<h2 class="section-title" style="top:816px">OUR SERVICES</h2>
<div class="svc blue" style="left:165px;top:913px">
  <svg width="60" height="50" viewBox="0 0 60 50" fill="none" stroke="#fff" stroke-width="2"><path d="M6 46V20L30 6l24 14v26z"/><path d="M6 46h48"/><rect x="16" y="26" width="14" height="20"/><circle cx="42" cy="36" r="7"/></svg>
  <h3>Lorem ipsum dolor sit</h3>
  <p>Lorem ipsum dolor sit consectetur adipiscing &nbsp;sed do eiusmod tempor incididunt &nbsp;labore dolore magna.</p>
  <div class="more">LEARN MORE <span class="dot"></span></div>
</div>
<div class="svc clay" style="left:450px;top:913px">
  <svg width="60" height="50" viewBox="0 0 60 50" fill="none" stroke="#fff" stroke-width="2"><circle cx="24" cy="16" r="10"/><path d="M8 46c0-10 7-16 16-16s16 6 16 16"/><circle cx="44" cy="28" r="7"/><path d="M34 46c0-6 4-10 10-10s10 4 10 10"/></svg>
  <h3>Lorem ipsum dolor sit</h3>
  <p>Lorem ipsum dolor sit consectetur adipiscing &nbsp;sed do eiusmod tempor incididunt &nbsp;labore dolore magna.</p>
  <div class="more">LEARN MORE <span class="dot"></span></div>
</div>
<div class="svc blue" style="left:734px;top:913px">
  <svg width="60" height="50" viewBox="0 0 60 50" fill="none" stroke="#fff" stroke-width="2"><rect x="6" y="24" width="48" height="22"/><path d="M12 24v22M20 24v22M28 24v22M36 24v22M44 24v22"/><rect x="10" y="6" width="16" height="12"/><circle cx="44" cy="12" r="6"/></svg>
  <h3>Lorem ipsum dolor sit</h3>
  <p>Lorem ipsum dolor sit consectetur adipiscing &nbsp;sed do eiusmod tempor incididunt &nbsp;labore dolore magna.</p>
  <div class="more">LEARN MORE <span class="dot"></span></div>
</div>

<section class="abs about"></section>
<div class="abs about-frame"></div>
<div class="abs about-block"></div>
<div class="abs about-photo" role="img" aria-label="Photo of a courtyard with plants, low seats and woven poufs"></div>
<h2 class="abs about-title">ABOUT US</h2>
<p class="abs about-text">Lorem ipsum dolor sit amet, consectetur adipiscing elit, sed do eiusmod tempor incididunt ut labore et dolore magna aliqua. Ut enim ad minim veniam, quis nostrud exercitation ullamco laboris nisi ut aliquip ex ea commodo consequat. Duis aute irure dolor in reprehenderit in voluptate velit esse cillum dolore eu fugiat nulla pariatur. Excepteur sint occaecat cupidatat non proident, sunt in culpa qui officia deserunt mollit anim id est laborum"Lorem ipsum dolor sit amet, consectetur adipiscing elit, sed do eiusmod tempor incididunt ut labore et dolore magna aliqua. Ut enim ad minim veniam, quis nostrud exercitation ullamco laboris nisi ut aliquip ex ea</p>
<div class="btn about-btn">LEARN MORE <span class="dot"></span></div>

<h2 class="section-title" style="top:1934px">OUR GALLERY</h2>
<div class="abs gallery">
  <div role="img" aria-label="Photo of an arched wall niche with dried flowers" style="background:linear-gradient(135deg,#b9a9a0,#8f8276 50%,#c79d8c)"></div>
  <div role="img" aria-label="Photo of children playing in a colourful playroom" style="background:linear-gradient(135deg,#f1ede6,#e8d8b8 50%,#d9a66a)"></div>
  <div role="img" aria-label="Photo of a nursery room with a painted tree and round rug" style="background:linear-gradient(135deg,#b7c9c6,#d8cdb8 50%,#c3a07d)"></div>
  <div role="img" aria-label="Photo of a cosy reading corner with a daybed" style="background:linear-gradient(135deg,#8a7563,#d9d2c7 55%,#b9ab98)"></div>
  <div role="img" aria-label="Photo of a bright conservatory full of potted plants" style="background:linear-gradient(135deg,#dfe6e2,#6f8a55 50%,#3f5a33)"></div>
  <div role="img" aria-label="Photo of a teacher reading to children seated on a blue carpet" style="background:linear-gradient(135deg,#c9d7e8,#4a6fb8 55%,#2f4f9a)"></div>
</div>
<div class="btn view-clay">VIEW MORE <span class="dot"></span></div>

<svg class="abs" style="left:0;top:2640px" width="1200" height="572" viewBox="0 0 1200 572" preserveAspectRatio="none">
  <path d="M0 100 C200 30 300 -20 500 50 S850 130 1000 60 S1150 40 1200 30 V572 H0Z" fill="var(--ice)"/>
  <path d="M0 140 C220 70 340 40 520 90 S860 150 1020 95 S1160 80 1200 75 V572 H0Z" fill="var(--blue-2)"/>
  <path d="M0 180 C200 120 360 100 540 140 S880 190 1040 140 S1170 130 1200 128 V572 H0Z" fill="var(--blue)"/>
</svg>
<h2 class="section-title" style="top:2788px;color:#fff">OUR TESTIMONIALS</h2>
<div class="arrow" style="left:60px;top:3000px;transform:rotate(45deg)"></div>
<div class="arrow" style="left:1122px;top:3000px;transform:rotate(-135deg)"></div>
<div class="card" style="left:166px;top:2898px">
  <div class="name">Maren T</div><div class="stars">&#9733;&#9733;&#9733;&#9733;&#9733;</div>
  <p>Lorem ipsum dolor sit amet consectetur adipiscing &nbsp;eiusmod tempor incididunt labore dolore magna aliquat enim minim veniam quis nostrud exercitation ullamco laboris nisi ut aliquip ex commodoad.</p>
  <span class="quote">&#8220;</span>
</div>
<div class="avatar" role="img" aria-label="Portrait photo of a parent with child" style="left:120px;top:2952px;background:linear-gradient(135deg,#e6c2a8,#a8735a)"></div>
<div class="card" style="left:672px;top:2898px">
  <div class="name">Maren T</div><div class="stars">&#9733;&#9733;&#9733;&#9733;&#9733;</div>
  <p>Lorem ipsum dolor sit amet consectetur adipiscing &nbsp;eiusmod tempor incididunt labore dolore magna aliquat enim minim veniam quis nostrud exercitation ullamco laboris nisi ut aliquip ex commodoad.</p>
  <span class="quote">&#8220;</span>
</div>
<div class="avatar" role="img" aria-label="Portrait photo of a parent with child" style="left:626px;top:2952px;background:linear-gradient(135deg,#e9d3c0,#8f6e58)"></div>

<h2 class="section-title" style="top:3282px">LATEST BLOG</h2>
<article class="abs blog-main">
  <div class="img" role="img" aria-label="Photo of a teacher and children building with colourful blocks"></div>
  <h4>perspiciatis unde omnis iste natus error volupt</h4>
  <div class="meta"><span>&#128197; 28 Apr 2023</span><span class="sep">|</span><span>&#128100; Ellis Varn</span></div>
  <p>Learn from scent detection expert Dario Pell, how cognition tests can help you improve your results.</p>
</article>
<article class="blog-item" style="top:3375px">
  <div class="img" role="img" aria-label="Photo of a bright classroom" style="background:linear-gradient(135deg,#cfe3ea,#9fb89a 55%,#7b6a54)"></div>
  <div><h5>Lorem ipsum dolor sit onsectetur</h5><div class="meta"><span>&#128197; 28 Apr 2023</span><span class="sep">|</span><span>&#128100; Ellis Varn</span></div><p>Sed ut perspiciatis unde omnis iste natus error sit voluptatem</p></div>
</article>
<article class="blog-item" style="top:3532px">
  <div class="img" role="img" aria-label="Photo of a plant-filled terrace" style="background:linear-gradient(135deg,#a9b88f,#c98a6c 55%,#5f7048)"></div>
  <div><h5>Lorem ipsum dolor sit onsectetur</h5><div class="meta"><span>&#128197; 28 Apr 2023</span><span class="sep">|</span><span>&#128100; Ellis Varn</span></div><p>Sed ut perspiciatis unde omnis iste natus error sit voluptatem</p></div>
</article>
<article class="blog-item" style="top:3690px">
  <div class="img" role="img" aria-label="Photo of a cosy reading corner" style="background:linear-gradient(135deg,#8a7563,#d9d2c7 55%,#b9ab98)"></div>
  <div><h5>Lorem ipsum dolor sit onsectetur</h5><div class="meta"><span>&#128197; 28 Apr 2023</span><span class="sep">|</span><span>&#128100; Ellis Varn</span></div><p>Sed ut perspiciatis unde omnis iste natus error sit voluptatem</p></div>
</article>
<div class="btn view-blue">VIEW MORE <span class="dot"></span></div>

<svg class="abs" style="left:0;top:4020px" width="1200" height="248" viewBox="0 0 1200 248" preserveAspectRatio="none">
  <path d="M0 70 C180 20 300 0 480 40 S820 90 1000 40 S1150 10 1200 20 V248 H0Z" fill="var(--clay)"/>
  <path d="M0 95 C200 45 330 30 500 65 S840 110 1010 65 S1160 45 1200 50 V248 H0Z" fill="var(--sky)"/>
</svg>
<h2 class="abs news-title">SUBSCRIBE TO NEWSLETTER</h2>
<div class="field" style="left:190px">Name</div>
<div class="field" style="left:495px">Email Address</div>
<div class="btn submit">SUBMIT NOW</div>

<footer class="abs footer"></footer>
<div class="abs foot-brand"><span class="mark"></span>Olvenbrook</div>
<span class="social" style="left:163px"></span>
<span class="social" style="left:205px"></span>
<span class="social" style="left:248px"></span>
<div class="col" style="left:442px;color:#fff"><h6>OtherLinks</h6><a>Home</a><a>About Us</a><a>Services</a><a>Testimonials</a><a>Blog</a><a>Contact Us</a></div>
<div class="col" style="left:631px;color:#fff"><h6>Other Links</h6><a>Legal Information</a><a>Terms &amp; Condition</a><a>Privacy Policy</a><a>Support</a><a>Site Map</a></div>
<div class="col" style="left:864px;color:#fff;width:240px"><h6>Contact Us</h6>
  <div class="contact-row"><svg width="14" height="14" viewBox="0 0 24 24" fill="var(--sky)"><path d="M6.6 10.8a15 15 0 0 0 6.6 6.6l2.2-2.2c.3-.3.7-.4 1-.2 1.1.4 2.3.6 3.6.6.6 0 1 .4 1 1V20c0 .6-.4 1-1 1A17 17 0 0 1 3 4c0-.6.4-1 1-1h3.5c.6 0 1 .4 1 1 0 1.3.2 2.5.6 3.6.1.3 0 .7-.2 1z"/></svg><div><b>Phone</b><span>+1 888 888 8888</span></div></div>
  <div class="contact-row"><svg width="14" height="14" viewBox="0 0 24 24" fill="var(--sky)"><path d="M2 5h20v14H2z"/><path d="M2 5l10 8 10-8" stroke="#232323" stroke-width="2" fill="none"/></svg><div><b>Email</b><span>info@olvenbrook.example.com</span></div></div>
  <div class="contact-row"><svg width="14" height="14" viewBox="0 0 24 24" fill="var(--sky)"><path d="M12 2a7 7 0 0 0-7 7c0 5 7 13 7 13s7-8 7-13a7 7 0 0 0-7-7zm0 9.5A2.5 2.5 0 1 1 12 6.5a2.5 2.5 0 0 1 0 5z"/></svg><div><b>Location</b><span>777 Lorem ipsum dolor sit amet, consectetur adipiscing elit,</span></div></div>
</div>
<div class="abs foot-line"></div>
<div class="abs copy">&copy; 2023 Olvenbrook &nbsp; | &nbsp; All Rights Reserved &nbsp;|</div>

</body>
</html>
```